Picking winner today! Design a Flyer for a Residential Cleaning Company - Quill Meadow

I am going to pick a winner in the next 4 hours!

I need a flyer to market to residents in residential buildings with renters. I have a premium cleaning company that offers a way to get a quote online, book online, and pay online all within 60 seconds.

I also have a 100% Hoppiness, Guaranteed!

You can pull any information you want from this website as well [login to view URL]

It needs to fit on a regular sheet of printer paper, 8.5 x 11.

I have added my logo to use as well and would like to incorporate the content below somewhere in the flyer

We are a service first company that specializes in Residential and Commercial Cleaning. We hop the extra mile to make sure you’re satisfied every step of the way! We offer affordable cleaning in Chicago, with a booking and payment system that is very easy and convenient to use! We believe in taking the extra time and steps necessary to make sure a clean house is the last thing you have to worry about. Do yourself a favor, and let us take pride in cleaning your home! Please email Marcus@[login to view URL] for your specific coupon code for your apartment complex!

I would also like [login to view URL] to appear somewhere on the flyer as well.

Please message me if you have any questions, thanks!

```html
<!DOCTYPE html>
<html lang="en">
<head>
<meta charset="utf-8">
<title>Quill Meadow – Residential &amp; Commercial Cleaning Flyer</title>
<link href="https://fonts.googleapis.com/css2?family=Roboto:wght@300;400;500;700&display=swap" rel="stylesheet">
<style>
  :root {
    --pink: #e6508a;
    --pink-soft: #f08cb4;
    --grey-text: #4a4a4a;
    --grey-num: #bcbcbc;
    --grey-panel: #e6e6e6;
    --white: #ffffff;
    --ink: #222222;
  }
  * { margin: 0; padding: 0; box-sizing: border-box; }
  html, body { width: 933px; height: 1200px; overflow: hidden; background: var(--white); }
  body { font-family: 'Roboto', Arial, sans-serif; color: var(--grey-text); }
  .flyer { position: relative; width: 933px; height: 1200px; background: var(--white); overflow: hidden; }

  .brand { position: absolute; left: 70px; top: 118px; display: flex; align-items: center; gap: 10px; }
  .brand-dot { width: 22px; height: 22px; border-radius: 50%; background: var(--pink); }
  .brand-name { font-size: 34px; font-weight: 700; color: var(--ink); letter-spacing: 0.5px; }
  .brand-tag { position: absolute; left: 72px; top: 164px; font-size: 10px; font-weight: 700; color: var(--ink); letter-spacing: 0.6px; }

  .hero-photo {
    position: absolute; left: 342px; top: 0; width: 591px; height: 663px;
    background: linear-gradient(150deg, #e9e2cf 0%, #c9ccd0 35%, #9fb0c3 60%, #d8cfb6 100%);
    clip-path: polygon(30% 3%, 100% 0, 100% 100%, 62% 97%, 35% 86%, 22% 70%, 14% 55%, 0 38%, 10% 30%, 8% 12%);
  }

  .headline { position: absolute; left: 62px; top: 302px; font-weight: 300; text-transform: uppercase; }
  .headline .big { display: block; font-size: 40px; color: var(--pink-soft); line-height: 48px; }
  .headline .mid { display: block; font-size: 24px; color: var(--pink-soft); line-height: 38px; }
  .headline .dark { display: block; font-size: 24px; color: var(--grey-text); font-weight: 400; line-height: 40px; }

  .section-head { position: absolute; display: flex; align-items: flex-start; gap: 22px; }
  .section-num { font-size: 46px; font-weight: 700; color: var(--grey-num); line-height: 46px; }
  .section-title { font-size: 20px; line-height: 22px; text-transform: uppercase; }
  .section-title .accent { display: block; color: var(--pink); font-weight: 500; }
  .section-title .plain { display: block; color: var(--grey-text); font-weight: 300; }
  .who-head { left: 70px; top: 530px; }
  .what-head { left: 362px; top: 788px; }

  .body-copy { position: absolute; font-size: 13.5px; line-height: 16.5px; color: var(--grey-text); font-weight: 400; }
  .body-copy .lead { color: var(--pink); font-weight: 700; }
  .who-copy { left: 70px; top: 598px; width: 240px; }
  .what-copy { left: 362px; top: 837px; width: 240px; font-size: 13.3px; }

  .panel { position: absolute; top: 791px; height: 269px; background: var(--grey-panel); }
  .panel-mascot { left: 0; width: 324px; }
  .mascot-art {
    position: absolute; left: 40px; top: 12px; width: 210px; height: 245px;
    background: radial-gradient(ellipse at 55% 50%, #ffffff 0%, #f6dbe6 60%, #e6e6e6 100%);
    border-radius: 12px;
  }
  .panel-services { left: 628px; width: 305px; padding: 22px 0 0 68px; }
  .services-title { font-size: 22px; font-weight: 500; color: var(--ink); margin-bottom: 6px; }
  .services-list { list-style: none; }
  .services-list li { display: flex; align-items: center; gap: 8px; height: 34px; font-size: 17px; font-weight: 300; color: var(--ink); margin-left: -22px; }
  .services-list svg { flex: none; }

  .contact-bar {
    position: absolute; left: 259px; top: 1092px; width: 408px; height: 108px;
    background: var(--pink); color: var(--white); text-align: center; padding-top: 24px;
  }
  .contact-email { font-size: 24px; font-weight: 300; line-height: 30px; }
  .contact-web { font-size: 17px; font-weight: 300; line-height: 24px; }
</style>
</head>
<body>
<main class="flyer">
  <div class="brand"><span class="brand-dot"></span><span class="brand-name">Quill Meadow</span></div>
  <div class="brand-tag">RESIDENTIAL &amp; COMMERCIAL CLEANING</div>

  <div class="hero-photo" role="img" aria-label="Photo of a smiling cleaner in a uniform shirt, leaning on her arm"></div>

  <h1 class="headline">
    <span class="big">Online</span>
    <span class="mid">Quotes, Bookings</span>
    <span class="mid">and Payment</span>
    <span class="dark">Just 60 Seconds</span>
  </h1>

  <div class="section-head who-head">
    <span class="section-num">01</span>
    <h2 class="section-title"><span class="accent">Who</span><span class="plain">We Are</span></h2>
  </div>
  <p class="body-copy who-copy"><span class="lead">Your Cleaning Company</span><br>We are a service first company that specializes in Residential and Commercial Cleaning. We hop the extra mile to make sure you're satisfied every step of the way!</p>

  <div class="panel panel-mascot">
    <div class="mascot-art" role="img" aria-label="Cartoon rabbit mascot holding a push broom"></div>
  </div>

  <div class="section-head what-head">
    <span class="section-num">02</span>
    <h2 class="section-title"><span class="accent">What</span><span class="plain">We Do</span></h2>
  </div>
  <p class="body-copy what-copy"><span class="lead">We offer addordable cleaning</span><br>in Chicago, with a booking and payment system that is very easy and convenient to use! We believe in taking the extra time and steps necessary to make sure a clean house is the last thing you have to worry about.<br><span class="lead">Do yourself a favor,</span><br>and let us take pride in cleaning your home! Please email Marcus@QuillMeadowChicago.com for your specific coupon code for your apartment complex!</p>

  <section class="panel panel-services">
    <h2 class="services-title">OUR SERVICES</h2>
    <ul class="services-list">
      <li><svg width="16" height="16" viewBox="0 0 16 16"><path d="M2 2 L12 12 M9 14 L14 9" stroke="#e6508a" stroke-width="2" fill="none" stroke-linecap="round"/></svg>Residential Cleaning</li>
      <li><svg width="16" height="16" viewBox="0 0 16 16"><path d="M2 2 L12 12 M9 14 L14 9" stroke="#e6508a" stroke-width="2" fill="none" stroke-linecap="round"/></svg>Hassel Free Scheduling</li>
      <li><svg width="16" height="16" viewBox="0 0 16 16"><path d="M2 2 L12 12 M9 14 L14 9" stroke="#e6508a" stroke-width="2" fill="none" stroke-linecap="round"/></svg>Convenient Payment</li>
      <li><svg width="16" height="16" viewBox="0 0 16 16"><path d="M2 2 L12 12 M9 14 L14 9" stroke="#e6508a" stroke-width="2" fill="none" stroke-linecap="round"/></svg>We Bring All Supplies</li>
      <li><svg width="16" height="16" viewBox="0 0 16 16"><path d="M2 2 L12 12 M9 14 L14 9" stroke="#e6508a" stroke-width="2" fill="none" stroke-linecap="round"/></svg>Move In/Out Cleaning</li>
      <li><svg width="16" height="16" viewBox="0 0 16 16"><path d="M2 2 L12 12 M9 14 L14 9" stroke="#e6508a" stroke-width="2" fill="none" stroke-linecap="round"/></svg>Commercial Cleaning</li>
    </ul>
  </section>

  <footer class="contact-bar">
    <div class="contact-email">Marcus@QuillMeadowChicago.com</div>
    <div class="contact-web">www.QuillMeadowChicago.com</div>
  </footer>
</main>
</body>
</html>
```